Echoes Beyond The Willow Poster

So Last year One of the Great Designers from here Came up with a poster for my Events... But Now it is Time to freshen it up.. I have attached the original poster.. I would like the Same wording.. Same Picture of me,. Just fresh Design and colours for the new event year ahead.
This Poster Will be used in Theatres and Hall to Advertise our Event so it needs to stand out but still remain classy
I would Also need The Final Version to be delivered in PhotoShop Version so That I Can Alter Things like the Venue Name, Date, and Ticket Details,, As they change all the time.
Industry/Entity Type
Events
Colors
Designer to choose colors to be used in the design.
Look and feel
Each slider illustrates characteristics of the customer's brand and the style your logo design should communicate.

```html
<!DOCTYPE html>
<html lang="en">
<head>
<meta charset="utf-8">
<title>Echoes Beyond The Willow – Poster</title>
<link rel="stylesheet" href="https://fonts.googleapis.com/css2?family=Playfair+Display:ital,wght@0,700;1,500&family=Raleway:wght@500;600;700;800&display=swap">
<style>
  :root {
    --backdrop: #e3e8e9;
    --night: #151a33;
    --night-deep: #090c1a;
    --glow: #3a3f6e;
    --gold: #caa661;
    --gold-soft: #e2c88f;
    --ivory: #f4eee1;
    --mist: #a9aecb;
    --band-ink: #14182c;
  }
  * { margin: 0; padding: 0; box-sizing: border-box; }
  html, body {
    width: 1200px; height: 1200px; overflow: hidden;
    background: var(--backdrop);
  }
  .poster {
    position: absolute;
    left: 300px; top: 176px;
    width: 600px; height: 848px;
    overflow: hidden;
    background:
      radial-gradient(ellipse 70% 45% at 50% 30%, var(--glow) 0%, rgba(58,63,110,0) 70%),
      linear-gradient(180deg, var(--night) 0%, var(--night-deep) 100%);
  }
  .frame {
    position: absolute; inset: 14px 14px 70px 14px;
    border: 1px solid var(--gold);
    opacity: 0.7;
    pointer-events: none;
  }
  .eyebrow {
    position: absolute; left: 0; right: 0; top: 36px;
    text-align: center;
    font-family: "Raleway", sans-serif;
    font-size: 12px; font-weight: 600; letter-spacing: 6px;
    color: var(--gold-soft); line-height: 1;
  }
  .portrait-arch {
    position: absolute; left: 130px; top: 68px;
    width: 340px; height: 412px;
    border-radius: 170px 170px 0 0;
    background:
      radial-gradient(ellipse 40% 28% at 50% 30%, rgba(196,160,140,0.85), rgba(196,160,140,0) 100%),
      linear-gradient(180deg, #4a4d6e 0%, #3a3c52 45%, #23252f 75%, rgba(9,12,26,0.95) 100%);
  }
  .arch-line {
    position: absolute; left: 118px; top: 56px;
    width: 364px; height: 424px;
  }
  .title {
    position: absolute; left: 0; right: 0; top: 498px;
    text-align: center;
    font-family: "Playfair Display", serif;
    color: var(--ivory);
  }
  .title-word {
    display: block;
    font-size: 56px; font-weight: 700; letter-spacing: 4px;
    line-height: 60px; height: 60px;
  }
  .title-link {
    display: block;
    font-style: italic; font-weight: 500;
    font-size: 22px; line-height: 28px; height: 28px;
    color: var(--gold);
  }
  .divider {
    position: absolute; left: 250px; top: 666px;
    width: 100px; height: 1px; background: var(--gold);
  }
  .billing {
    position: absolute; left: 0; right: 0;
    text-align: center;
    font-family: "Raleway", sans-serif;
    line-height: 1;
  }
  .role { top: 682px; font-size: 12px; font-weight: 600; letter-spacing: 3.5px; color: var(--mist); }
  .performer { top: 702px; font-size: 34px; font-weight: 800; letter-spacing: 4px; color: var(--ivory); }
  .date { top: 748px; font-size: 16px; font-weight: 700; letter-spacing: 2.5px; color: var(--gold-soft); }
  .date sup { font-size: 9px; }
  .venue-band {
    position: absolute; left: 0; right: 0; bottom: 0; height: 56px;
    background: var(--gold);
    display: flex; align-items: center; justify-content: center;
  }
  .venue {
    font-family: "Raleway", sans-serif;
    font-size: 11.5px; font-weight: 700; letter-spacing: 0.8px;
    color: var(--band-ink); white-space: nowrap;
  }
</style>
</head>
<body>
  <main class="poster">
    <div class="frame"></div>
    <p class="eyebrow">AN EVENING OF MEDIUMSHIP</p>

    <div class="portrait-arch" role="img" aria-label="Photograph of the medium in a dark suit, reaching a hand out towards the viewer"></div>
    <svg class="arch-line" viewBox="0 0 364 424" aria-hidden="true">
      <path d="M0.5 424 V182 A181.5 181.5 0 0 1 363.5 182 V424" fill="none" stroke="#caa661" stroke-width="1"/>
    </svg>

    <h1 class="title">
      <span class="title-word">ECHOES</span>
      <span class="title-link">beyond the</span>
      <span class="title-word">WILLOW</span>
    </h1>
    <div class="divider"></div>

    <p class="billing role">RENOWNED SPIRITUALIST MEDIUM</p>
    <p class="billing performer">RHYS CALLOWAY</p>
    <p class="billing date">MONDAY 21<sup>st</sup> NOVEMBER</p>

    <div class="venue-band">
      <p class="venue">LARKFIELD PLAYHOUSE BRYNMOOR; FOR TICKETS CALL BOX OFFICE 01700</p>
    </div>
  </main>
</body>
</html>
```